Kelekeleoliolimaiwaipeleke Fish Package

We need a package design for our Kelekeleoliolimaiwaipeleke Fish (not Bravlin fish). We plan to sell them at Hawaii stores to start and them take them to the mainland. We are looking for a package design that includes the front with a Kelekeleoliolimaiwaipeleke Fish (not a photo) and a back design with a photo of the fish (we will supply), information about the fish and nutrition information.

Target Market(s)

Premium market

Colors

Designer to choose colors to be used in the design.

Requirements
Must have
• See attached overview - also, it must include our logo (which we will provide)
Nice to have
• See attached overview

```html
<!DOCTYPE html>
<html lang="en">
<head>
<meta charset="utf-8">
<title>Kelekeleoliolimaiwaipeleke Fish Package Front</title>
<link rel="stylesheet" href="https://fonts.googleapis.com/css2?family=Oswald:wght@500;600&display=swap">
<style>
  :root {
    --bg: #e9e9e9;
    --maroon-deep: #5c0a0e;
    --maroon: #8d1117;
    --red-bright: #e8263b;
    --tab-white: #ffffff;
    --logo-red: #e0263a;
    --band-grey: #6b6b6b;
    --ocean-light: #2f6fa8;
    --ocean-mid: #1d4f8c;
    --ocean-deep: #0f2d6a;
    --fish-light: #e4e2dc;
    --fish-mid: #9a9288;
    --text-light: #ffffff;
  }
  * { margin: 0; padding: 0; box-sizing: border-box; }
  html, body {
    width: 900px; height: 1200px; overflow: hidden;
    background: var(--bg);
  }
  .package {
    position: relative;
    width: 900px; height: 1200px;
    background: linear-gradient(160deg, var(--maroon) 0%, var(--maroon-deep) 70%);
    font-family: "Oswald", "Arial Narrow", sans-serif;
    color: var(--text-light);
    overflow: hidden;
  }
  .package-art { position: absolute; inset: 0; }
  .logo-tab {
    position: absolute;
    left: 125px; top: 0;
    width: 643px; height: 254px;
    background: var(--tab-white);
    border-radius: 0 0 34px 34px;
    display: flex; align-items: center; justify-content: center;
  }
  .brand-name {
    font-weight: 600;
    font-size: 104px;
    letter-spacing: 6px;
    color: var(--logo-red);
    line-height: 1;
    padding-top: 40px;
  }
  .product-title {
    position: absolute;
    left: 0; right: 0; top: 322px;
    text-align: center;
    font-weight: 500;
    font-size: 54px;
    letter-spacing: -0.5px;
    line-height: 1;
  }
  .tagline-band {
    position: absolute;
    left: 71px; top: 427px;
    width: 760px; height: 140px;
    background: var(--band-grey);
    padding: 22px 0 0 22px;
  }
  .tagline {
    font-weight: 500;
    font-size: 37px;
    line-height: 1.3;
    letter-spacing: -0.3px;
  }
  .product-facts {
    position: absolute;
    left: 0; width: 900px; top: 1022px;
    text-align: center;
    font-weight: 500;
    font-size: 29px;
    line-height: 1.35;
  }
</style>
</head>
<body>
  <main class="package">
    <svg class="package-art" width="900" height="1200" viewBox="0 0 900 1200">
      <defs>
        <linearGradient id="oceanGradient" x1="0" y1="0" x2="0.3" y2="1">
          <stop offset="0" stop-color="var(--ocean-light)"/>
          <stop offset="0.5" stop-color="var(--ocean-mid)"/>
          <stop offset="1" stop-color="var(--ocean-deep)"/>
        </linearGradient>
        <radialGradient id="fishGradient" cx="0.55" cy="0.5" r="0.5">
          <stop offset="0" stop-color="var(--fish-light)"/>
          <stop offset="0.7" stop-color="var(--fish-mid)" stop-opacity="0.8"/>
          <stop offset="1" stop-color="var(--ocean-mid)" stop-opacity="0"/>
        </radialGradient>
      </defs>
      <path class="ocean-backdrop" role="img"
            aria-label="Blue underwater reef backdrop"
            d="M0,930 C300,700 640,560 900,490 L900,1200 L0,1200 Z"
            fill="url(#oceanGradient)"/>
      <path class="swoosh" d="M900,390 C640,480 300,620 0,860 L0,930 C300,700 640,560 900,490 Z" fill="var(--red-bright)"/>
      <ellipse class="fish-photo" role="img"
               aria-label="Photo of a striped Hawaiian reef triggerfish swimming to the right"
               cx="470" cy="835" rx="280" ry="140"
               fill="url(#fishGradient)"/>
    </svg>

    <div class="logo-tab">
      <span class="brand-name">WAVO LEI</span>
    </div>

    <h1 class="product-title">KELEKELEOLIOLIMAIWAIPELEKE FISH</h1>

    <div class="tagline-band">
      <p class="tagline">PREMIUM KELEKELEOLIOLIMAIWAIPELEKE<br>FISH A HAWAIIAN TREAT</p>
    </div>

    <p class="product-facts">PINEAPPLE, CITRUS AND RASPBERRY<br>NET WEIGHT 5.0 OZ</p>
  </main>
</body>
</html>
```